Funk up our website

Our website is currently in operation and working well, see it at www.clearbriefhub.co.uk

However it needs some redesign work, to help it feel fresh, inviting and friendly.

We need graphic mockups (png hi-res) to pass to the dev team, to do the css work:

homepage - http://www.clearbriefhub.co.uk
topic page - http://www.clearbriefhub.co.uk/guidance/business
sub-topic - http://www.clearbriefhub.co.uk/guidance/business/goods-services
content - http://www.clearbriefhub.co.uk/guidance/business/goods-services/heads-of-terms
ancillary pages - contact us, heads of terms, etc

The structure of the page in terms of the placement of header, menu bar, content area and footer needs to remain, but the design of it is up for grabs.

The site is currently free to use, but in the future will have the aim of getting users to register for free, but with the option of buying documents on an individual basis, or subscription basis, or subscribing to additional legal services.

Additional information
---------------------------
Users
1. Owners and managers in small and medium businesses
2. In the UK only
3. Who find dealing with legal issues and lawyers intimidating
4. Who are searching for online help to try and avoid having to deal with a lawyer
5. Or have been referred via social media
Desired user experience
1. A welcoming, friendly site
2. That takes the complexity out of dealing with legal issues
3. That really does clear the brief
4. That is fast, efficient and clear
5. That is pleasantly different from the normal experience of interacting with a law firm
Relevant factors
1. Most visitors will first land on a content page (e.g. [link]) via a search result or banner advertisement – not the Home Page
2. Repeat visitors are more likely to go to the Home Page
3. Works with web responsive design techniques for display on smartphones and tablets
4. Implemented through CSS
Colour palette
Designer should feel able to build the palette around the following core colours
CMYK
YELLOW = 0,25,100,0
GREEN = 80,0,100,0
BLUE = 100,25,0,0

RGB
YELLOW = 255,195,15
GREEN = 15,175,75
BLUE = 0,140,210

PANTONE
YELLOW = 123c
GREEN = 361c
BLUE = 3005c

Fonts
Soho Gothic, Soho, Arial
Designer should feel able to add fonts to complement these core fonts.

Our logo needs to remain (see attached document) Our strap line, can be changed if needed.

Best
RK
Updates

Hi All

Some websites worth having a look at for how people have done things differently / added something distinctive to their website:

http://www.brevicounsel.co.uk/
https://www.tandelegal.co.uk/
http://www.quillatrix.com/

Cheers
RK

Hi All

Thanks for your designs. Just back in the office today, we will discuss and feedback / decide asap.

Best
RK

```html
<!DOCTYPE html>
<html lang="en">
<head>
<meta charset="utf-8">
<title>ClearBrief Hub – Home</title>
<link href="https://fonts.googleapis.com/css2?family=Arimo:wght@400;700&family=Fira+Sans:wght@400&family=Archivo+Black&display=swap" rel="stylesheet">
<style>
:root{
  --yellow:#ffc30f;
  --green:#0faf4b;
  --blue:#008cd2;
  --heading-blue:#1a8ad0;
  --text:#333;
  --muted:#555;
  --band:#f6f6f6;
  --footer:#efefef;
  --line:#e2e2e2;
}
*{box-sizing:border-box;margin:0;padding:0}
html,body{width:1043px;height:1200px;overflow:hidden;background:#fff}
body{position:relative;font-family:Arimo,Arial,sans-serif;color:var(--text)}
.abs{position:absolute}

.tagline{left:111px;top:14px;font-family:"Fira Sans",Arial,sans-serif;font-size:15.5px;line-height:19px;color:#222}
.tagline .sub{display:block;padding-left:42px}
.tagline .y{color:var(--yellow)}.tagline .g{color:var(--green)}.tagline .b{color:var(--blue)}

.search{left:562px;top:33px;width:191px;height:19px;border:1px solid #ddd;border-radius:3px;background:#fafafa;font-size:10px;color:#aaa;padding:3px 4px}
.search svg{position:absolute;right:5px;top:2px}
.btn{top:30px;height:24px;border-radius:3px;color:#fff;font-size:11px;display:flex;align-items:center;justify-content:center}
.btn-register{left:768px;width:76px;background:var(--green)}
.btn-login{left:852px;width:77px;background:var(--blue)}

.nav{left:113px;top:63px;width:816px;height:63px;border:1px solid #e6e6e6;background:linear-gradient(#fff,#f1f1f1);display:flex}
.brand{width:265px;display:flex;align-items:center;padding-left:10px;gap:8px}
.brand-mark{width:30px;height:30px;background:var(--green);border-radius:50%}
.brand-name{font-size:20px;font-weight:700;color:#333;line-height:1}
.nav ul{list-style:none;display:flex;height:100%}
.nav li{height:100%;display:flex;align-items:center;padding:0 15px;font-size:12.5px;font-weight:700;color:#444;border-left:1px solid #e4e4e4}
.nav li.active{background:var(--yellow);color:#fff;border-left:none;padding:0 11px}

.hero{left:112px;top:137px;width:817px;height:295px;border-radius:3px;background:linear-gradient(100deg,#6a3a1c 0%,#b9753b 35%,#d9a15d 55%,#8a5428 80%,#4b2b14 100%)}
.hero h1{position:absolute;left:49px;top:110px;font-family:"Archivo Black",Arial,sans-serif;font-weight:400;font-size:21.5px;line-height:25px;color:#fff;letter-spacing:.6px}
.dots{position:absolute;left:15px;top:267px;display:flex;gap:3px}
.dots span{width:10px;height:10px;border-radius:50%;background:#444}
.dots span:first-child{background:var(--green)}

.feedback{left:1002px;top:378px;width:41px;height:123px;background:var(--green);border-radius:3px 0 0 3px;color:#fff;font-weight:700;font-size:14px;writing-mode:vertical-rl;transform:rotate(180deg);display:flex;align-items:center;justify-content:center}

.section-title{font-size:15.5px;color:var(--heading-blue);font-weight:400}
.welcome-title{left:107px;top:484px}
.videos-title{left:594px;top:484px}
.welcome-text{left:114px;top:518px;width:469px;font-size:10.6px;line-height:20.9px;text-align:justify;color:#333}

.video{left:600px;top:515px;width:330px;height:188px;border-radius:3px;background:linear-gradient(90deg,#3b1d12,#7a5031 45%,#a07848 60%,#4a3020);overflow:hidden}
.play{position:absolute;left:148px;top:83px;width:35px;height:22px;background:rgba(0,0,0,.6);border-radius:3px}
.play:after{content:"";position:absolute;left:14px;top:6px;border-left:9px solid #fff;border-top:5px solid transparent;border-bottom:5px solid transparent}
.progress{position:absolute;left:25px;top:158px;width:220px;height:7px;border:1px solid #999;background:#222}
.progress i{display:block;width:32%;height:100%;background:var(--blue)}
.side-icons{position:absolute;right:17px;top:16px;display:flex;flex-direction:column;gap:4px}
.side-icons span{width:24px;height:17px;background:rgba(0,0,0,.65);border-radius:2px}

.band{left:0;top:735px;width:1043px;height:384px;background:var(--band)}
.testimonials-title{left:112px;top:775px}
.experts-title{left:392px;top:775px}
.news-title{left:670px;top:775px}

.quote-mark{left:108px;top:800px;font-family:Georgia,serif;font-size:42px;color:#aaa;line-height:1}
.testimonial{left:124px;top:838px;width:240px;font-size:10.6px;line-height:20.9px;text-align:justify;color:#444}
.person-name{font-size:12px;font-weight:700;color:var(--green)}
.person-role{font-size:10.6px;color:#444}
.t-name{left:124px;top:990px}.t-role{left:124px;top:1011px}

.expert-photo{left:391px;top:833px;width:87px;height:79px;background:linear-gradient(#5b6470,#8b8f94 55%,#2e3138)}
.e-name{left:488px;top:854px}.e-role{left:488px;top:876px}
.expert-text{left:393px;top:920px;width:258px;font-size:10.6px;line-height:20.9px;text-align:justify;color:#444}
.read-more{left:391px;top:1008px;width:61px;height:17px;background:var(--green);color:#fff;font-size:10.6px;border-radius:2px;display:flex;align-items:center;justify-content:center}

.news-thumb{left:668px;width:72px;height:70px}
.n1{top:833px;background:linear-gradient(#f1ead8,#b5835a 60%,#5a3520)}
.n2{top:951px;background:linear-gradient(#3a2210,#a2642c 55%,#2d1808)}
.news-text{left:755px;width:175px;font-size:10.6px;line-height:20.9px;text-align:justify;color:#444}
.news-text a{color:var(--green);text-decoration:none}
.nt1{top:830px}.nt2{top:946px}
.news-date{left:755px;font-size:10.6px;font-weight:700;color:#333}
.d1{top:920px}.d2{top:1036px}

.chat{left:805px;top:1087px;width:124px;height:32px;background:var(--blue);color:#fff;font-size:12px;font-weight:700;display:flex;align-items:center;justify-content:center;gap:9px}

.footer{left:0;top:1119px;width:1043px;height:81px;background:var(--footer)}
.footer-links{left:113px;top:1144px;font-size:12.5px;color:#333;word-spacing:2px}
.footer-links span{color:#555;margin:0 7px}
.copyright{left:113px;top:1175px;font-size:12.5px;color:#333}
.social{top:1151px;width:31px;height:30px;border-radius:2px}
.s1{left:815px;background:#2ea3e0}.s2{left:858px;background:#1d6fa8}.s3{left:898px;background:#3d5a98}
</style>
</head>
<body>

<div class="abs tagline">Making legal services<span class="sub"><span class="y">fast,</span> <span class="g">efficient</span> <span class="b">&amp; clear.</span></span></div>

<div class="abs search">Search
  <svg width="14" height="14" viewBox="0 0 14 14"><circle cx="5.5" cy="5.5" r="4" fill="none" stroke="#777" stroke-width="1.6"/><line x1="8.5" y1="8.5" x2="13" y2="13" stroke="#777" stroke-width="2"/></svg>
</div>
<div class="abs btn btn-register">Register</div>
<div class="abs btn btn-login">Login</div>

<nav class="abs nav">
  <div class="brand"><span class="brand-mark"></span><span class="brand-name">ClearBrief Hub</span></div>
  <ul>
    <li class="active">Home</li>
    <li>Guide yourself</li>
    <li>Draft yourself</li>
    <li>Search for a lawyer</li>
    <li>Get your drafts</li>
  </ul>
</nav>

<section class="abs hero" role="img" aria-label="Brass scales of justice in a warm, softly blurred courtroom">
  <h1>FREE LEGAL SUPPORT FOR<br>YOU &amp; YOUR BUSINESS</h1>
  <div class="dots"><span></span><span></span><span></span><span></span></div>
</section>

<div class="abs feedback">Feedback</div>

<h2 class="abs section-title welcome-title">Welcome to ClearBrief Hub</h2>
<h2 class="abs section-title videos-title">Featured Videos</h2>

<p class="abs welcome-text">Lorem Ipsum is simply dummy text of the printing and typesetting industry. Lorem Ipsum has been the industry's standard dummy text ever since the 1500s, when an unknown printer took a galley of type and scrambled it to make a type specimen book. It has survived not only five centuries, but also the leap into electronic typesetting, remaining essentially unchanged. It was popularised in the 1960s with the release of Letraset sheets containing Lorem Ipsum passages, and more recently with desktop publishing software like Aldus PageMaker including versions of Lorem Ipsum.<br>Lorem Ipsum is simply dummy text of the printing and typesetting industry. Lorem Ipsum has been the industry's standard dummy text ever since the 1500s, when an unknown printer took a galley of type and scrambled it to make a type specimen book. It has survived not only five centuries,</p>

<div class="abs video" role="img" aria-label="Video still of scales of justice in front of shelves of law books">
  <div class="side-icons"><span></span><span></span><span></span><span></span></div>
  <div class="play"></div>
  <div class="progress"><i></i></div>
</div>

<div class="abs band"></div>

<h2 class="abs section-title testimonials-title">Clients Testimonials</h2>
<h2 class="abs section-title experts-title">Legal Experts</h2>
<h2 class="abs section-title news-title">Latest News</h2>

<div class="abs quote-mark">&ldquo;</div>
<p class="abs testimonial">Sed ut perspiciatis unde omnis iste natus error sit voluptatem accusantium doloremque laudantium, totam rem aperiam, eaque ipsa quae ab illo inventore veritatis et quasi architecto beatae vitae dicta sunt explicabo. Nemo enim ipsam voluptatem quia voluptas sit</p>
<div class="abs person-name t-name">Daniel Marsh</div>
<div class="abs person-role t-role">Legal Advisor ,ClearBrief Hub</div>

<div class="abs expert-photo" role="img" aria-label="Portrait photo of the legal expert"></div>
<div class="abs person-name e-name">Peter Hollis</div>
<div class="abs person-role e-role">Legal Advisor ,ClearBrief Hub</div>
<p class="abs expert-text">Perspiciatis unde omnis iste natus error sit voluptatem accusantium doloremque laudantium, totam rem aperiam, eaque ipsa quae ab illo inventore veritatis et quasi architecto beatae vitae dicta sunt explicabo.</p>
<div class="abs read-more">Read More</div>

<div class="abs news-thumb n1" role="img" aria-label="Wooden gavel on a sound block"></div>
<p class="abs news-text nt1">Perspiciatis unde omnis iste natus error sit voluptatem accusantium doloremque aperiam, eaque ipsa quae ab illo inventore <a>... Read More</a></p>
<div class="abs news-date d1">Date : 13-12-2013</div>

<div class="abs news-thumb n2" role="img" aria-label="Stacked old books with an hourglass"></div>
<p class="abs news-text nt2">Perspiciatis unde omnis iste natus error sit voluptatem accusantium doloremque aperiam, eaque ipsa quae ab illo inventore <a>... Read More</a></p>
<div class="abs news-date d2">Date : 13-12-2013</div>

<div class="abs chat">
  <svg width="20" height="14" viewBox="0 0 20 14"><ellipse cx="10" cy="6" rx="9.5" ry="5.5" fill="#fff"/><path d="M4 9 L2 14 L8 10 Z" fill="#fff"/></svg>
  Online Chat
</div>

<footer class="abs footer"></footer>
<div class="abs footer-links">Home<span>|</span>Guide yourself<span>|</span>Draft yourself<span>|</span>Search for a lawyer<span>|</span>Get your drafts</div>
<div class="abs copyright">Copyright 2013 ,All Rights Reserved</div>
<div class="abs social s1"></div>
<div class="abs social s2"></div>
<div class="abs social s3"></div>

</body>
</html>
```